THE BRAMWELL GROUP
CHANGING THE WAY THE STAFFING INDUSTRY DOES BUSINESS, ONE RELATIONSHIP AT A TIME
Professional
Ted Harnack
Principal
2380 Fernhollow Road
3rd Floor
Berwyn, PA 19477
tdh@bramwellgroupllc.example
www.bramwellgroupllc.example
We provide three basic services: Temporary Staffing, Temp-to-Perm, and Direct Placement. I was originally going to list these as bullet points on the back of the card, but I'm trying to save money on printing costs. I don't think this info will fit properly on the front, but if it could fit without clogging things up, that would be interesting. I'd also like to use the word "mobile" instead of "cell".

```html
<!DOCTYPE html>
<html lang="en">
<head>
<meta charset="utf-8">
<title>The Bramwell Group — Stationery</title>
<link href="https://fonts.googleapis.com/css2?family=Libre+Baskerville:wght@400&family=Open+Sans:wght@400;600&display=swap" rel="stylesheet">
<style>
  :root {
    --stage: #e8e3da;
    --paper: #ffffff;
    --blue: #1f4fa8;
    --blue-deep: #123a86;
    --blue-light: #d9e3f4;
    --ink: #2d3440;
    --muted: #7b8494;
    --rule: #c9ced8;
    --label: #3c3a36;
  }
  * { box-sizing: border-box; margin: 0; padding: 0; }
  html, body { width: 1200px; height: 662px; overflow: hidden; }
  body { background: var(--stage); font-family: "Open Sans", sans-serif; color: var(--ink); position: relative; }

  .piece { position: absolute; background: var(--paper); box-shadow: 0 2px 6px rgba(0,0,0,.18); overflow: hidden; }
  .piece-label { position: absolute; font-size: 9px; color: var(--label); text-align: center; width: 100%; top: -14px; white-space: nowrap; }
  .wrap { position: absolute; }

  .brand { font-family: "Libre Baskerville", serif; color: var(--blue); font-weight: 400; letter-spacing: .04em; white-space: nowrap; display: flex; align-items: center; gap: 6px; }
  .brand-dot { width: 12px; height: 12px; border-radius: 50%; background: var(--blue); flex: none; }
  .brand-tag { font-size: 4.5px; color: var(--muted); letter-spacing: .06em; margin-top: 2px; text-transform: uppercase; }

  .side-band { position: absolute; left: 0; top: 0; bottom: 0; width: 22px; background: linear-gradient(90deg, var(--blue-deep), var(--blue)); }
  .sheet-head { position: absolute; left: 60px; top: 30px; }
  .sheet-head .brand { font-size: 15px; }
  .sheet-foot { position: absolute; left: 30px; right: 8px; bottom: 10px; font-size: 5px; color: var(--muted); text-align: center; }

  /* fax */
  .fax-title { position: absolute; right: 14px; top: 98px; font-size: 8px; font-weight: 600; color: var(--ink); }
  .fax-form { position: absolute; left: 34px; top: 110px; width: 278px; border-collapse: collapse; font-size: 6px; table-layout: fixed; }
  .fax-form td { border: 1px solid var(--rule); height: 17px; padding: 0 4px; }
  .fax-form .field { width: 34px; background: #f3f5f9; }
  .fax-checks { position: absolute; left: 34px; width: 278px; top: 194px; display: flex; justify-content: space-between; font-size: 5.5px; white-space: nowrap; }
  .fax-checks span::before { content: ""; display: inline-block; width: 6px; height: 6px; border: 1px solid var(--muted); margin-right: 3px; vertical-align: -1px; }

  /* envelopes */
  .env-front .brand { font-size: 13px; position: absolute; left: 34px; top: 24px; }
  .env-front .return { position: absolute; left: 34px; top: 52px; font-size: 5px; color: var(--muted); line-height: 1.5; }
  .env-back svg { position: absolute; inset: 0; }
  .env-back .brand { position: absolute; left: 50%; top: 26px; transform: translateX(-50%); font-size: 11px; }
  .env-back .brand.on-blue { color: #fff; }
  .env-back .brand.on-blue .brand-dot { background: #fff; }
  .env-back .brand .brand-dot { width: 9px; height: 9px; }

  /* card */
  .card-left { position: absolute; left: 0; top: 0; bottom: 0; width: 52%; padding: 0 5px; display: flex; align-items: center; justify-content: center; flex-direction: column; }
  .card-left .brand { font-size: 5px; gap: 2px; letter-spacing: .02em; }
  .card-left .brand-dot { width: 5px; height: 5px; }
  .card-left .brand-tag { font-size: 2.6px; width: 78px; text-align: center; letter-spacing: .03em; line-height: 1.3; }
  .card-right { position: absolute; right: 0; top: 0; bottom: 0; width: 48%; background: linear-gradient(160deg, var(--blue), var(--blue-deep)); color: #fff; padding: 9px 5px 6px 6px; font-size: 4.3px; line-height: 1.45; white-space: nowrap; }
  .card-right .name { font-size: 6.5px; font-weight: 600; }
  .card-right .role { margin-bottom: 4px; opacity: .85; }
</style>
</head>
<body>

  <!-- business card -->
  <div class="wrap" style="left:1003px; top:30px; width:178px; height:92px;">
    <div class="piece-label">Business Card (Front)</div>
    <div class="piece" style="inset:0;">
      <div class="card-left">
        <div class="brand"><span class="brand-dot"></span>THE BRAMWELL GROUP</div>
        <div class="brand-tag">Changing the way the staffing industry does business, one relationship at a time</div>
      </div>
      <div class="card-right">
        <div class="name">Ted Harnack</div>
        <div class="role">Principal</div>
        <div>Office (610) 555-0142</div>
        <div>Mobile (610) 555-0187</div>
        <div>tdh@bramwellgroupllc.example</div>
        <div>www.bramwellgroupllc.example</div>
        <div style="margin-top:3px;">2380 Fernhollow Road, 3rd Floor<br>Berwyn, PA 19477</div>
      </div>
    </div>
  </div>

  <!-- fax cover -->
  <div class="wrap" style="left:34px; top:210px; width:326px; height:434px;">
    <div class="piece-label">Fax Cover</div>
    <div class="piece" style="inset:0;">
      <div class="side-band"></div>
      <div class="sheet-head">
        <div class="brand"><span class="brand-dot"></span>THE BRAMWELL GROUP</div>
        <div class="brand-tag">Changing the way the staffing industry does business, one relationship at a time</div>
      </div>
      <div class="fax-title">FAX</div>
      <table class="fax-form">
        <tr><td class="field">To:</td><td></td><td class="field">From:</td><td></td></tr>
        <tr><td class="field">Fax:</td><td></td><td class="field">Pages:</td><td></td></tr>
        <tr><td class="field">Phone:</td><td></td><td class="field">Date:</td><td></td></tr>
        <tr><td class="field">Re:</td><td></td><td class="field">CC:</td><td></td></tr>
      </table>
      <div class="fax-checks">
        <span>Urgent</span><span>For Review</span><span>Please Comment</span><span>Please Reply</span><span>Please Recycle</span>
      </div>
      <div class="sheet-foot">2380 Fernhollow Road · 3rd Floor · Berwyn, PA 19477 · (610) 555-0142 · www.bramwellgroupllc.example · tdh@bramwellgroupllc.example</div>
    </div>
  </div>

  <!-- letterhead -->
  <div class="wrap" style="left:396px; top:210px; width:326px; height:434px;">
    <div class="piece-label">Letterhead</div>
    <div class="piece" style="inset:0;">
      <div class="side-band"></div>
      <div class="sheet-head">
        <div class="brand"><span class="brand-dot"></span>THE BRAMWELL GROUP</div>
        <div class="brand-tag">Changing the way the staffing industry does business, one relationship at a time</div>
      </div>
      <div class="sheet-foot">2380 Fernhollow Road · 3rd Floor · Berwyn, PA 19477 · (610) 555-0142 · www.bramwellgroupllc.example · tdh@bramwellgroupllc.example</div>
    </div>
  </div>

  <!-- envelope front -->
  <div class="wrap" style="left:768px; top:210px; width:408px; height:222px;">
    <div class="piece-label">Envelopes (Front)</div>
    <div class="piece env-front" style="inset:0;">
      <div class="side-band" style="width:16px;"></div>
      <div class="brand"><span class="brand-dot"></span>THE BRAMWELL GROUP</div>
      <div class="return">2380 Fernhollow Road, 3rd Floor<br>Berwyn, PA 19477</div>
    </div>
  </div>

  <!-- envelope back option 1 -->
  <div class="wrap" style="left:768px; top:463px; width:408px; height:100px;">
    <div class="piece-label">Envelopes (Back): Option 1</div>
    <div class="piece env-back" style="inset:0;">
      <svg width="408" height="100" viewBox="0 0 408 100">
        <path d="M0 0 L204 62 L408 0" fill="none" stroke="var(--blue-light)" stroke-width="10"/>
        <path d="M0 0 L204 62 L408 0" fill="none" stroke="var(--blue)" stroke-width="1.5"/>
      </svg>
      <div class="brand" style="top:14px;"><span class="brand-dot"></span>THE BRAMWELL GROUP</div>
    </div>
  </div>

  <!-- envelope back option 2 -->
  <div class="wrap" style="left:768px; top:588px; width:408px; height:60px;">
    <div class="piece-label">Envelopes (Back): Option 2</div>
    <div class="piece env-back" style="inset:0;">
      <svg width="408" height="60" viewBox="0 0 408 60">
        <path d="M0 0 H408 V10 L204 58 L0 10 Z" fill="var(--blue)"/>
      </svg>
      <div class="brand on-blue" style="top:12px;"><span class="brand-dot"></span>THE BRAMWELL GROUP</div>
    </div>
  </div>

</body>
</html>
```